Label design for Kombucha bottles

I'm in the process of making a new brand of Kombucha called Wren Kombucha. Looking for something minimal, but with character.
NOTE: Kombucha is not a beer, it's a fermented flavoured tea which is a healthy alternative to soft drink - and as such doesn't contain any alcohol and is sugar-free.
The label can incorporate "The Quiet Lantern" logo if you so wish (not essential), also came up with a rough idea of a firey barrel idea to get you started, but interested in any other ideas. (On second thoughts disregard this, don't put in quiet lantern logo)
Specifications wise: the label will go on the front of a 330ml beer bottle on an oval-shaped label. Would be good to have examples on a bottle to reference the size of the design. Only for a size guide see the Tallbrook label
Target Market(s)
Hipster crowd
Logo Text
Wren Kombucha
Logo styles of interest
Character Logo
Colors
Designer to choose colors to be used in the design.
Look and feel

```html
<!DOCTYPE html>
<html lang="en">
<head>
<meta charset="utf-8">
<title>Wren Kombucha – Bottle Labels</title>
<link rel="stylesheet" href="https://fonts.googleapis.com/css2?family=Oswald:wght@500;700&family=Kalam:wght@400&display=swap">
<style>
  :root {
    --canvas-bg: #ecebe6;
    --mojito-ring-light: #5fc4b4;
    --mojito-ring-dark: #2d8e9a;
    --grape-ring-light: #4e5b86;
    --grape-ring-dark: #2b3357;
    --label-yellow: #f2e23a;
    --label-yellow-deep: #e3c825;
    --ink-brown: #4a2a17;
    --arc-text: #f4e6a8;
    --barrel-green: #6a9a2e;
  }
  * { margin: 0; padding: 0; box-sizing: border-box; }
  html, body { width: 1200px; height: 770px; overflow: hidden; }
  body {
    background: var(--canvas-bg);
    display: flex;
    align-items: center;
    justify-content: space-around;
    padding: 0 90px;
  }
  .bottle-label { width: 360px; height: 480px; display: block; }
  .flavour-arc { font-family: "Oswald", sans-serif; font-weight: 700; font-size: 15px; letter-spacing: 2px; fill: var(--arc-text); }
  .tagline { font-family: "Oswald", sans-serif; font-weight: 700; font-size: 18px; letter-spacing: 2px; fill: var(--ink-brown); }
  .brand-name { font-family: "Oswald", sans-serif; font-weight: 700; font-size: 46px; letter-spacing: 1px; fill: var(--ink-brown); }
  .fine-print { font-family: "Kalam", cursive; font-size: 13px; fill: var(--ink-brown); }
  .claim { font-family: "Oswald", sans-serif; font-weight: 700; font-size: 22px; fill: var(--ink-brown); letter-spacing: 1px; }
</style>
</head>
<body>

<svg class="bottle-label label-mojito" viewBox="0 0 360 480" aria-label="Wren Kombucha mojito flavour label">
  <defs>
    <linearGradient id="mojito-ring" x1="0" y1="0" x2="0" y2="1">
      <stop offset="0" stop-color="var(--mojito-ring-light)"/>
      <stop offset="1" stop-color="var(--mojito-ring-dark)"/>
    </linearGradient>
    <radialGradient id="mojito-field" cx="0.5" cy="0.45" r="0.6">
      <stop offset="0" stop-color="var(--label-yellow)"/>
      <stop offset="1" stop-color="var(--label-yellow-deep)"/>
    </radialGradient>
    <path id="mojito-top-arc" d="M 40 240 A 140 200 0 0 1 320 240"/>
  </defs>
  <ellipse class="label-ring" cx="180" cy="240" rx="172" ry="232" fill="url(#mojito-ring)"/>
  <ellipse class="label-field" cx="180" cy="244" rx="140" ry="194" fill="url(#mojito-field)"/>
  <text class="flavour-arc"><textPath href="#mojito-top-arc" startOffset="50%" text-anchor="middle">MOJITO FLAVOUR</textPath></text>
  <text class="tagline" x="180" y="126" text-anchor="middle">ALL NATURAL</text>
  <text class="brand-name" x="180" y="200" text-anchor="middle">WREN</text>
  <text class="brand-name" x="180" y="254" text-anchor="middle">KOMBUCHA</text>
  <text class="fine-print" x="118" y="286" text-anchor="middle">Homebrewed</text>
  <text class="fine-print" x="245" y="286" text-anchor="middle">Net 330 ml</text>
  <rect class="barrel-art" x="148" y="300" width="64" height="88" rx="14" fill="var(--barrel-green)" role="img" aria-label="Illustration of a fiery barrel"/>
  <text class="claim" x="110" y="352" text-anchor="middle">SUGAR</text>
  <text class="claim" x="252" y="352" text-anchor="middle">FREE</text>
</svg>

<svg class="bottle-label label-grape" viewBox="0 0 360 480" aria-label="Wren Kombucha grape flavour label">
  <defs>
    <linearGradient id="grape-ring" x1="0" y1="0" x2="0" y2="1">
      <stop offset="0" stop-color="var(--grape-ring-light)"/>
      <stop offset="1" stop-color="var(--grape-ring-dark)"/>
    </linearGradient>
    <radialGradient id="grape-field" cx="0.5" cy="0.45" r="0.6">
      <stop offset="0" stop-color="var(--label-yellow)"/>
      <stop offset="1" stop-color="var(--label-yellow-deep)"/>
    </radialGradient>
    <path id="grape-top-arc" d="M 40 240 A 140 200 0 0 1 320 240"/>
  </defs>
  <ellipse class="label-ring" cx="180" cy="240" rx="172" ry="232" fill="url(#grape-ring)"/>
  <ellipse class="label-field" cx="180" cy="244" rx="140" ry="194" fill="url(#grape-field)"/>
  <text class="flavour-arc"><textPath href="#grape-top-arc" startOffset="50%" text-anchor="middle">GRAPE FLAVOUR</textPath></text>
  <text class="tagline" x="180" y="126" text-anchor="middle">ALL NATURAL</text>
  <text class="brand-name" x="180" y="200" text-anchor="middle">WREN</text>
  <text class="brand-name" x="180" y="254" text-anchor="middle">KOMBUCHA</text>
  <text class="fine-print" x="118" y="286" text-anchor="middle">Homebrewed</text>
  <text class="fine-print" x="245" y="286" text-anchor="middle">Net 330 ml</text>
  <rect class="barrel-art" x="148" y="300" width="64" height="88" rx="14" fill="var(--barrel-green)" role="img" aria-label="Illustration of a fiery barrel"/>
  <text class="claim" x="110" y="352" text-anchor="middle">SUGAR</text>
  <text class="claim" x="252" y="352" text-anchor="middle">FREE</text>
</svg>

</body>
</html>
```